Coffee Cocktails Recipe Flips cards

create (12) recipe cards that illustrate the finished beverage, with its description, ingredients, and instructions. each card should be 5"x7" and styled to incorporate brand theme and the cultural elements of the beverage. cards will be used for stuffers in shipments of product, used by bartenders, and digitally shared. Present each drink in glassware that embodies the spirit of the culture it represents, garnishing with flair and a nod to the exotic origins, creating a multisensory experience that'll transport the drinker to distant lands with just one indulgent sip.
The presentation of each drink should reflect the cultural fusion aesthetically, using suggested glassware and garnishes to bring the exotic themes to life. Enjoy crafting these drinks and take your guests on a flavorful voyage around the world with each sip!

Target Market(s)

Consumers and Bars and Restaurants

Industry/Entity Type

coffee and adult beverages

Colors

Designer to choose colors to be used in the design.

Requirements
Must have
• brand alignment, styled to reflect the uniqueness of each recipe
Should not have
• appropriate glassware, garnishments, and images of raw ingredients

```html
<!DOCTYPE html>
<html lang="en">
<head>
<meta charset="utf-8">
<title>Café Mocha Bliss — Recipe Card</title>
<link rel="stylesheet" href="https://fonts.googleapis.com/css2?family=Quicksand:wght@700&family=Source+Sans+3:wght@300;700&display=swap">
<style>
  :root {
    --backdrop: #e9e9e9;
    --card-top: #6cc493;
    --card-mid: #3f826d;
    --card-bottom: #1c3140;
    --ink-light: #ffffff;
    --ink-soft: #e6f1ec;
    --tab-bg: #ffffff;
    --brand-ink: #1c3140;
    --brand-accent: #5cbf8a;
  }
  * { margin: 0; padding: 0; box-sizing: border-box; }
  html, body {
    width: 1200px;
    height: 1200px;
    overflow: hidden;
    background: var(--backdrop);
  }
  .recipe-card {
    position: absolute;
    left: 230px;
    top: 83px;
    width: 739px;
    height: 1034px;
    background: linear-gradient(180deg, var(--card-top) 0%, var(--card-mid) 42%, var(--card-bottom) 100%);
    color: var(--ink-light);
    font-family: "Source Sans 3", "Myriad Pro", sans-serif;
    overflow: hidden;
  }
  .brand-tab {
    position: absolute;
    left: 546px;
    top: 0;
    width: 148px;
    height: 202px;
    background: var(--tab-bg);
    border-radius: 0 0 74px 74px;
    display: flex;
    align-items: center;
    justify-content: center;
    gap: 8px;
    padding-top: 40px;
  }
  .brand-dot {
    width: 12px;
    height: 12px;
    border-radius: 50%;
    background: var(--brand-accent);
  }
  .brand-name {
    font-family: "Source Sans 3", sans-serif;
    font-weight: 700;
    font-size: 26px;
    color: var(--brand-ink);
  }
  .drink-title {
    position: absolute;
    left: 58px;
    top: 74px;
    font-family: "Quicksand", "Josefin Sans", sans-serif;
    font-weight: 700;
    line-height: 1;
  }
  .drink-title .title-main {
    display: block;
    font-size: 124px;
  }
  .drink-title .title-sub {
    display: block;
    font-size: 53px;
    margin-top: 12px;
    margin-left: 2px;
  }
  .drink-description {
    position: absolute;
    left: 58px;
    top: 293px;
    width: 640px;
    font-weight: 300;
    font-size: 18.5px;
    line-height: 24.6px;
    color: var(--ink-soft);
  }
  .leaf-decoration {
    position: absolute;
    left: 414px;
    top: 473px;
    width: 325px;
    height: 561px;
    background: radial-gradient(closest-side at 55% 45%, rgba(108,196,147,0.34) 0%, rgba(108,196,147,0.12) 60%, rgba(108,196,147,0) 100%);
  }
  .section-heading {
    position: absolute;
    left: 58px;
    font-weight: 700;
    font-size: 23px;
    line-height: 28px;
  }
  .ingredients-heading { top: 502px; }
  .instructions-heading { top: 748px; }
  .ingredient-list, .step-list {
    position: absolute;
    list-style: none;
    font-weight: 300;
    font-size: 18.5px;
    line-height: 24.6px;
    color: var(--ink-soft);
  }
  .ingredient-list { left: 70px; top: 542px; }
  .ingredient-list li::before { content: "• "; }
  .step-list { left: 57px; top: 789px; width: 645px; }
  .step-list li {
    padding-left: 17px;
    text-indent: -17px;
  }
</style>
</head>
<body>
  <article class="recipe-card">
    <div class="brand-tab">
      <span class="brand-dot"></span>
      <span class="brand-name">Verda</span>
    </div>

    <h1 class="drink-title">
      <span class="title-main">Café</span>
      <span class="title-sub">Mocha Bliss</span>
    </h1>

    <p class="drink-description">Indulge in the balance of bittersweet espresso entwined with rich chocolate syrup to enjoy the luxe texture of the Café Mocha Bliss. Gently pour the espresso into your favorite mug, caress it with the velvety touch of chocolate, and crown the mix with steamed milk as soft as clouds. End with a swirl of whipped cream, graced with a sprinkling of chocolate shavings or a delicate dusting of cocoa powder—your canvas of comfort.</p>

    <div class="leaf-decoration" role="img" aria-label="Botanical line illustration of leafy vines climbing the lower right of the card"></div>

    <h2 class="section-heading ingredients-heading">Ingredients:</h2>
    <ul class="ingredient-list">
      <li>5g Verda Classic Black Coffee</li>
      <li>8oz hot water</li>
      <li>2 tablespoons chocolate syrup</li>
      <li>Steamed milk</li>
      <li>Whipped cream</li>
      <li>Chocolate shavings for garnish</li>
    </ul>

    <h2 class="section-heading instructions-heading">Instructions:</h2>
    <ol class="step-list">
      <li>1. Mix 8oz of hot water with one packet Verda Classic Black Instant Coffee, mix well until powder is fully dissolved.</li>
      <li>2. Pour the Coffee into a mug.</li>
      <li>3. Stir in the chocolate syrup until well combined.</li>
      <li>4. Top with steamed milk.</li>
      <li>5. Add a generous dollop of whipped cream.</li>
      <li>6. Garnish with chocolate shavings.</li>
    </ol>
  </article>
</body>
</html>
```